Ecard for facebook and Instagram postings

I need 4 ecards (don't know if that is what it is called) for Facebook and Instagram postings. My Logo and company name should be incorporated and also be square. I would like to be able to insert text as I need. Examples are:

https://www.pictoralhub.com/photo.php?fbid=20262841672382489&set=a.20261729249182489.516031.71298967488&type=1&relevant_count=1

https://media-b-ord.yy.imgvaultcdn.net/hpics-tin4/2345967_657092986477056_308792573_n.jpg

I don't necessarily need images on them, just the color scheme to my business cards and the logo and business name. But if you'd like to give it an interesting look, you can go ahead and play with it. My site is lunaroakcoaching.com, if you'd like to see the style of it.

Thank you!!!
Updates

I just uploaded the logo in two variations.  Thank you!

Target Market(s)

Women 16-65

Industry/Entity Type

Business

Requirements
Must have
• Logo and business name
Should not have
• No white background. I have attached business card picture so you can have an idea of what I'd like.

```html
<!DOCTYPE html>
<html lang="en">
<head>
<meta charset="utf-8">
<title>Lunar Oak Coaching Services – Quote Card</title>
<link rel="stylesheet" href="https://fonts.googleapis.com/css2?family=Tinos:wght@700&family=Open+Sans:wght@400&display=swap">
<style>
  :root {
    --peach-light: #fdf1e2;
    --peach-edge: #f8cc96;
    --orange: #f7941d;
    --orange-soft: #f9ab4c;
    --orange-deep: #ef7d10;
    --crimson: #c1272d;
    --ink: #0c0c0c;
    --white: #ffffff;
  }
  html, body {
    margin: 0;
    padding: 0;
    overflow: hidden;
    background: var(--peach-edge);
  }
  .quote-card {
    position: relative;
    width: 1200px;
    height: 1200px;
    overflow: hidden;
    font-family: "Tinos", "Times New Roman", serif;
  }
  .card-texture {
    position: absolute;
    inset: 0;
    background: radial-gradient(ellipse at 50% 42%, var(--peach-light) 0%, #fbe2c4 55%, var(--peach-edge) 100%);
  }
  .top-band {
    position: absolute;
    left: 0; top: 0;
    width: 1200px; height: 17px;
    background: var(--orange);
  }
  .quote-mark {
    position: absolute;
    margin: 0;
    color: var(--crimson);
    font-weight: 700;
    font-size: 330px;
    line-height: 1;
  }
  .quote-mark--open { left: 58px; top: 60px; }
  .quote-mark--close { left: 948px; top: 800px; }
  .quote-text {
    position: absolute;
    left: 0; top: 218px;
    width: 1200px;
    margin: 0;
    text-align: center;
    color: var(--ink);
    font-weight: 700;
    font-size: 88px;
    line-height: 100px;
  }
  .footer-wave {
    position: absolute;
    left: 0; top: 0;
    width: 1200px; height: 1200px;
  }
  .brand-name {
    position: absolute;
    left: 50px; top: 1040px;
    margin: 0;
    color: var(--crimson);
    font-weight: 700;
    font-size: 74px;
    line-height: 1;
  }
  .brand-tagline {
    position: absolute;
    left: 54px; top: 1128px;
    margin: 0;
    color: var(--crimson);
    font-weight: 700;
    font-size: 30px;
    letter-spacing: 7px;
    line-height: 1;
  }
  .brand-site {
    position: absolute;
    left: 512px; top: 1130px;
    margin: 0;
    color: var(--white);
    font-family: "Open Sans", Arial, sans-serif;
    font-size: 29px;
    letter-spacing: 1px;
    line-height: 1;
  }
  .brand-badge {
    position: absolute;
    left: 1018px; top: 1010px;
    width: 156px; height: 156px;
    border-radius: 50%;
    background: var(--orange-deep);
    border: 6px solid var(--white);
    box-sizing: border-box;
  }
</style>
</head>
<body>
  <main class="quote-card">
    <div class="card-texture" role="img" aria-label="Soft peach background with a fine crosshatch texture"></div>
    <div class="top-band"></div>

    <p class="quote-mark quote-mark--open" aria-hidden="true">“</p>
    <p class="quote-text">Ignorance is the<br>curse of God;<br>knowledge is the<br>wing wherewith we<br>fly to heaven</p>
    <p class="quote-mark quote-mark--close" aria-hidden="true">”</p>

    <svg class="footer-wave" viewBox="0 0 1200 1200" aria-hidden="true">
      <defs>
        <linearGradient id="footerFill" x1="0" y1="0" x2="0" y2="1">
          <stop offset="0" stop-color="#fab35a"/>
          <stop offset="1" stop-color="#f58a12"/>
        </linearGradient>
      </defs>
      <path d="M0,928 C320,900 720,930 1200,1050 L1200,1200 L0,1200 Z" fill="url(#footerFill)"/>
      <path d="M0,928 C320,900 720,930 1200,1050" fill="none" stroke="#ffffff" stroke-width="5"/>
      <path d="M0,952 C340,922 760,975 1200,1140 L1200,1160 C760,1000 340,945 0,972 Z" fill="#c1272d"/>
      <rect x="0" y="1175" width="1200" height="25" fill="#c1272d"/>
    </svg>

    <p class="brand-name">Lunar Oak</p>
    <p class="brand-tagline">COACHING SERVICES</p>
    <p class="brand-site">lunaroakcoaching.com</p>
    <div class="brand-badge" aria-hidden="true"></div>
  </main>
</body>
</html>
```